Innovative automotive company needs some flat designs

Hi there. This is your project brief that will tell you everything you need to know. We want to create a Facebook ad that tells a story about the benefits of using our platform. We have a compelling story. We have the words. Now we need the graphics.
Requirements:
Our company's brand identity has the following three elements, futuristic, premium and minimalistic. The design has to be like this too.
Our colour scheme is RGB (255,255,255), 73,225,245, and 5, 7, 9.
Here's our company's landing page. From there you may take a look at our app too.
www.velmorix.io
We have a great story to tell. Help us make it eye-catching. And engaging.
Here are the 4 points/images we want to bring across. Words in brackets should be included in the images.
Words should only take up AT MOST 20% of the space.
THERE SHOULD BE 4 IMAGES (1 FOR EACH POINT). PLEASE DO NOT USE THE ICONS THAT WE HAVE ON OUR WEBSITE. You can refer to the attached for reference. This is the kind of format that we want but the style should be suited to our company brand identity and colour scheme.
Each image should be 600 x 600 pixels
1) Quality Assurance
(3-tier screening to select partner workshops of all expertise. Regular audit and mystery shopping to ensure quality.)
2) Save time and effort
(For each requests, our system chooses the best offers and send them to you. Compare job scope, price, reviews, duration and others at a glance.)
3) No overcharging, no redundant repairs
(Job scope is pre-agreed through the app. Any changes have to be documented.
With these records, our in-house technical expertise and data analytics will identify bad behaviour.)
4) Community Reviews
(Reviews from consumers after each job is completed. Ensure high standards consistently.)

```html
<!DOCTYPE html>
<html lang="en">
<head>
<meta charset="utf-8">
<title>Velmorix – Save time and effort</title>
<link rel="stylesheet" href="https://fonts.googleapis.com/css2?family=Michroma&display=swap">
<style>
  :root {
    --ink: #05070a;
    --panel: #121a22;
    --panel-deep: #0a0f15;
    --cyan: #49e1f5;
    --white: #ffffff;
    --rule: #3a434c;
    --paper: #f4f5f6;
  }
  * { margin: 0; padding: 0; box-sizing: border-box; }
  html, body {
    width: 1200px;
    height: 1200px;
    overflow: hidden;
    background: var(--paper);
  }
  .ad {
    position: relative;
    width: 1200px;
    height: 1200px;
    overflow: hidden;
    font-family: "Michroma", sans-serif;
    color: var(--white);
  }
  .ad__sheet {
    position: absolute;
    inset: 0;
  }
  .brand {
    position: absolute;
    top: 118px;
    right: 64px;
    display: flex;
    align-items: center;
    gap: 22px;
    font-size: 50px;
    letter-spacing: 6px;
    text-transform: uppercase;
    color: var(--white);
  }
  .brand__mark {
    width: 26px;
    height: 26px;
    border-radius: 50%;
    background: var(--white);
  }
  .benefit {
    position: absolute;
    left: 84px;
    top: 376px;
    width: 860px;
  }
  .benefit__title {
    font-size: 34px;
    font-weight: 400;
    font-variant: small-caps;
    letter-spacing: 1px;
    line-height: 1;
    margin-bottom: 26px;
  }
  .benefit__title-initial {
    color: var(--cyan);
  }
  .benefit__text {
    font-size: 22px;
    font-variant: small-caps;
    line-height: 27px;
    letter-spacing: 0.5px;
  }
  .benefit__icon {
    position: absolute;
    left: 810px;
    top: 650px;
    width: 220px;
    height: 180px;
  }
  .ad__rule {
    position: absolute;
    left: 68px;
    top: 945px;
    width: 955px;
    height: 2px;
    background: linear-gradient(90deg, var(--rule), rgba(58,67,76,0.4));
  }
</style>
</head>
<body>
<main class="ad">
  <svg class="ad__sheet" viewBox="0 0 1200 1200" role="img" aria-label="Dim photograph of a car interior with dashboard and steering wheel">
    <defs>
      <radialGradient id="sheetShade" cx="0.42" cy="0.42" r="0.75">
        <stop offset="0" stop-color="#1a242e"/>
        <stop offset="0.6" stop-color="#121a22"/>
        <stop offset="1" stop-color="#0a0f15"/>
      </radialGradient>
    </defs>
    <polygon points="0,24 1200,0 1200,1200 30,1190 6,1130 0,740" fill="url(#sheetShade)"/>
  </svg>

  <div class="brand">
    <span class="brand__mark"></span>
    <span class="brand__name">Velmorix</span>
  </div>

  <section class="benefit">
    <h1 class="benefit__title"><span class="benefit__title-initial">S</span>ave time and effort</h1>
    <p class="benefit__text">
      For each requests, our system<br>
      chooses the best offers and send<br>
      them to you.&nbsp; Compare job scope, price,<br>
      reviews, duration and others at a glance.
    </p>
  </section>

  <svg class="benefit__icon" viewBox="0 0 220 180" aria-hidden="true">
    <rect x="18" y="10" width="184" height="152" rx="10" fill="var(--white)" transform="rotate(4 110 86)"/>
    <rect x="8" y="22" width="190" height="148" rx="10" fill="var(--cyan)" transform="rotate(-3 103 96)"/>
    <g fill="none" stroke="var(--ink)" stroke-width="9" stroke-linecap="round" stroke-linejoin="round">
      <path d="M143 96 A40 40 0 1 1 129 66"/>
      <polyline points="103,72 103,96 118,108"/>
    </g>
    <polygon points="134,92 152,92 143,108" fill="var(--ink)"/>
  </svg>

  <div class="ad__rule"></div>
</main>
</body>
</html>
```